KV PowerPoint Design

I need a slick PowerPoint template following my newly designed logo (see the attached ZIP file for logo details, fonts, and colors).
Please also see the Sample.pptx file for an idea of the simplicity and slickness I am after (do not consider the colors or fonts from the Sample file, just as an idea). Other ideas are very welcome.

```html
<!DOCTYPE html>
<html lang="en">
<head>
<meta charset="utf-8">
<title>KV Presentation Template – Slide Overview</title>
<link href="https://fonts.googleapis.com/css2?family=Montserrat:wght@400;500;700;800&display=swap" rel="stylesheet">
<style>
  :root{
    --bg:#f4f6fc;
    --navy:#0f1f8f;
    --deep:#030b5c;
    --royal:#1c36a6;
    --bright:#0a4fd6;
    --pale:#e5ebfb;
    --steel:#a6b6d4;
    --frame:#d3d6de;
    --select:#0b57d0;
    --white:#ffffff;
    --photo-a:#cfcfcf;
    --photo-b:#5a5a5a;
  }
  *{box-sizing:border-box;margin:0;padding:0}
  html,body{width:1200px;height:527px;overflow:hidden;background:var(--bg)}
  body{position:relative;font-family:"Montserrat",sans-serif;color:var(--navy)}

  .slide{position:absolute;width:352px;height:200px;background:var(--white);border:1.5px solid var(--frame);border-radius:12px;overflow:hidden}
  .slide.is-selected{border:none;box-shadow:0 0 0 3px var(--white),0 0 0 6px var(--select);}
  .slide-number{position:absolute;font-size:15px;color:#444;font-weight:400}

  .panel{position:absolute;left:5px;top:5px;right:5px;bottom:5px;border-radius:8px;background:linear-gradient(180deg,var(--royal) 0%,var(--deep) 100%);overflow:hidden}
  .is-selected .panel{left:0;top:0;right:0;bottom:0}

  .abs{position:absolute}
  .sq{position:absolute}
  .sq.steel{background:var(--steel)}
  .sq.pale{background:var(--pale)}
  .sq.navy{background:var(--royal)}
  .sq.bright{background:var(--bright)}
  .sq.mid{background:#1d37b0}
  .sq.gray{background:#dcdcdc}

  /* brand mark stand-in */
  .brand{position:absolute;display:flex;align-items:center;gap:4px;font-weight:800;color:var(--navy)}
  .brand .dot{border-radius:50%;background:currentColor}
  .brand.light{color:var(--white)}
  .brand.large{font-size:20px}
  .brand.large .dot{width:16px;height:16px}
  .brand.small{font-size:8px;gap:2px}
  .brand.small .dot{width:6px;height:6px}

  .eyebrow{font-size:9.6px;font-weight:400;white-space:nowrap}
  .title{font-weight:700;line-height:1.15}
  .title.xl{font-size:15.5px}
  .title.md{font-size:11.8px}
  .sub{font-size:7.4px;font-weight:400;white-space:nowrap}
  .on-dark{color:var(--white)}

  /* photo collage */
  .collage{position:absolute;width:145px;height:123px;transform-origin:0 0}
  .photo{position:absolute;background:linear-gradient(160deg,var(--photo-a),var(--photo-b))}

  .bars{position:absolute;left:64px;bottom:0;display:flex;height:7px}
  .bars span{width:72px}

  .toc{position:absolute;left:21px;top:78px;width:160px;list-style:none}
  .toc li{display:flex;align-items:baseline;font-size:5.8px;height:14.4px;color:var(--royal)}
  .toc .label{width:88px}
  .toc .leader{flex:1;border-bottom:0.6px dotted var(--royal);margin-right:3px}

  .agenda{position:absolute;left:22px;top:72px;list-style:none}
  .agenda li{font-size:7px;height:10.6px;color:var(--royal);letter-spacing:0.15px;display:flex}
  .agenda .n{width:15px}

  .big-number{font-size:30px;font-weight:800;color:var(--steel);letter-spacing:-1px}
</style>
</head>
<body>

<!-- Slide 1: title, light -->
<div class="slide" style="left:42px;top:34px">
  <div class="sq steel" style="left:320px;top:5px;width:27px;height:26px"></div>
  <div class="sq pale" style="left:291px;top:31px;width:29px;height:29px"></div>
  <div class="sq navy" style="left:320px;top:60px;width:28px;height:28px"></div>
  <div class="brand large" style="left:28px;top:114px"><span class="dot"></span>KV</div>
  <p class="eyebrow abs" style="left:105px;top:104px">Lorem ipsum dolor sit amet consectetur</p>
  <h1 class="title xl abs" style="left:105px;top:119px">Lorem ipsum dolor sit amet<br>consectetur</h1>
</div>
<span class="slide-number" style="left:42px;top:246px">1</span>

<!-- Slide 2: title, dark -->
<div class="slide" style="left:424px;top:34px">
  <div class="panel">
    <div class="sq steel" style="left:315px;top:0;width:28px;height:26px"></div>
    <div class="sq pale" style="left:286px;top:26px;width:29px;height:29px"></div>
    <div class="sq mid" style="left:315px;top:26px;width:28px;height:29px"></div>
    <div class="sq navy" style="left:315px;top:55px;width:28px;height:28px"></div>
    <div class="brand large light" style="left:28px;top:109px"><span class="dot"></span>KV</div>
    <p class="eyebrow abs on-dark" style="left:100px;top:99px">Lorem ipsum dolor sit amet consectetur</p>
    <h1 class="title xl abs on-dark" style="left:100px;top:114px">Lorem ipsum dolor sit amet<br>consectetur</h1>
    <div class="bars"><span style="background:var(--steel)"></span><span style="background:var(--royal)"></span><span style="background:var(--white)"></span></div>
  </div>
</div>
<span class="slide-number" style="left:424px;top:246px">2</span>

<!-- Slide 3: intro with people -->
<div class="slide" style="left:806px;top:34px">
  <div class="brand small" style="left:21px;top:30px;font-size:12px"><span class="dot" style="width:10px;height:10px"></span>KV</div>
  <div class="collage" style="left:202px;top:5px">
    <div class="sq bright" style="left:0;top:48px;width:31px;height:33px"></div>
    <div class="sq navy" style="left:31px;top:59px;width:31px;height:22px"></div>
    <div class="sq gray" style="left:31px;top:81px;width:31px;height:27px"></div>
    <div class="sq bright" style="left:120px;top:59px;width:25px;height:22px"></div>
    <div class="sq navy" style="left:120px;top:81px;width:25px;height:42px"></div>
    <div class="photo" role="img" aria-label="Portrait photo of a smiling woman" style="left:31px;top:0;width:61px;height:59px"></div>
    <div class="photo" role="img" aria-label="Portrait photo of a man with glasses" style="left:92px;top:0;width:53px;height:59px"></div>
    <div class="photo" role="img" aria-label="Portrait photo of a smiling young woman" style="left:62px;top:59px;width:58px;height:64px"></div>
  </div>
  <h2 class="title md abs" style="left:17px;top:114px">Lorem ipsum dolor sit amet<br>consectetur</h2>
  <p class="sub abs" style="left:17px;top:148px;color:var(--royal)">Lorem ipsum dolor sit amet consectetur</p>
</div>
<span class="slide-number" style="left:806px;top:246px">3</span>

<!-- Slide 4: contents -->
<div class="slide" style="left:42px;top:287px">
  <h2 class="title md abs" style="left:21px;top:21px">Lorem ipsum dolor sit amet<br>consectetur</h2>
  <p class="sub abs" style="left:21px;top:51px;color:var(--royal)">Lorem ipsum dolor sit amet consectetur</p>
  <ul class="toc">
    <li><span class="label">Lorem ipsum dolor sit</span><span class="leader"></span>1</li>
    <li><span class="label">Lorem ipsum dolor sit</span><span class="leader"></span>2</li>
    <li><span class="label">Lorem ipsum dolor sit</span><span class="leader"></span>3</li>
    <li><span class="label">Lorem ipsum dolor sit</span><span class="leader"></span>4</li>
    <li><span class="label">Lorem ipsum dolor sit</span><span class="leader"></span>5</li>
    <li><span class="label">Lorem ipsum dolor sit</span><span class="leader"></span>6</li>
  </ul>
  <div class="collage" style="left:235px;top:5px;transform:scale(.77)">
    <div class="sq bright" style="left:0;top:48px;width:31px;height:33px"></div>
    <div class="sq navy" style="left:31px;top:59px;width:31px;height:22px"></div>
    <div class="sq gray" style="left:31px;top:81px;width:31px;height:27px"></div>
    <div class="sq bright" style="left:120px;top:59px;width:25px;height:22px"></div>
    <div class="sq navy" style="left:120px;top:81px;width:25px;height:42px"></div>
    <div class="photo" role="img" aria-label="Portrait photo of a smiling woman" style="left:31px;top:0;width:61px;height:59px"></div>
    <div class="photo" role="img" aria-label="Portrait photo of a man with glasses" style="left:92px;top:0;width:53px;height:59px"></div>
    <div class="photo" role="img" aria-label="Portrait photo of a smiling young woman" style="left:62px;top:59px;width:58px;height:64px"></div>
  </div>
  <div class="brand small" style="left:320px;top:170px"><span class="dot"></span>KV</div>
</div>
<span class="slide-number" style="left:42px;top:499px">4</span>

<!-- Slide 5: section divider, dark -->
<div class="slide is-selected" style="left:428px;top:291px;width:344px;height:192px">
  <div class="panel">
    <p class="big-number abs" style="left:18px;top:26px">01</p>
    <h2 class="title md abs on-dark" style="left:18px;top:76px">Lorem ipsum dolor sit amet<br>consectetur</h2>
    <p class="abs on-dark" style="left:18px;top:110px;font-size:9.4px;white-space:nowrap">Lorem ipsum dolor sit amet consectetur</p>
    <div class="collage" style="left:231px;top:1px;transform:scale(.77)">
      <div class="sq bright" style="left:0;top:48px;width:31px;height:33px"></div>
      <div class="sq navy" style="left:31px;top:59px;width:31px;height:22px"></div>
      <div class="sq pale" style="left:31px;top:81px;width:31px;height:27px"></div>
      <div class="sq bright" style="left:120px;top:59px;width:25px;height:22px"></div>
      <div class="sq navy" style="left:120px;top:81px;width:25px;height:42px"></div>
      <div class="photo" role="img" aria-label="Portrait photo of a smiling woman" style="left:31px;top:0;width:61px;height:59px"></div>
      <div class="photo" role="img" aria-label="Portrait photo of a man with glasses" style="left:92px;top:0;width:53px;height:59px"></div>
      <div class="photo" role="img" aria-label="Portrait photo of a smiling young woman" style="left:62px;top:59px;width:58px;height:64px"></div>
    </div>
    <div class="brand small light" style="left:312px;top:168px"><span class="dot"></span>KV</div>
  </div>
</div>
<span class="slide-number" style="left:424px;top:499px">5</span>

<!-- Slide 6: numbered list -->
<div class="slide" style="left:806px;top:287px">
  <div class="sq steel" style="left:326px;top:5px;width:21px;height:21px"></div>
  <div class="sq pale" style="left:302px;top:26px;width:24px;height:22px"></div>
  <div class="sq navy" style="left:326px;top:48px;width:21px;height:23px"></div>
  <h2 class="title md abs" style="left:19px;top:21px">Lorem ipsum dolor sit amet</h2>
  <p class="sub abs" style="left:19px;top:43px;color:var(--royal)">Lorem ipsum dolor sit amet consectetur</p>
  <ol class="agenda">
    <li><span class="n">1.</span>Lorem ipsum dolor sit amet consectetur</li>
    <li><span class="n">2.</span>Lorem ipsum dolor sit amet consectetur</li>
    <li><span class="n">3.</span>Lorem ipsum dolor sit amet consectetur</li>
    <li><span class="n">4.</span>Lorem ipsum dolor sit amet consectetur</li>
    <li><span class="n">5.</span>Lorem ipsum dolor sit amet consectetur</li>
    <li><span class="n">6.</span>Lorem ipsum dolor sit amet consectetur</li>
    <li><span class="n">7.</span>Lorem ipsum dolor sit amet consectetur</li>
  </ol>
  <div class="brand small" style="left:320px;top:170px"><span class="dot"></span>KV</div>
</div>
<span class="slide-number" style="left:806px;top:499px">6</span>

</body>
</html>
```